Maple Crest Tutoring General Flyer Design

Reason: We are very close to making a selection but would like to provide a little more time for some of the designers to complete their revisions.
Target Market(s)
Secondary school students
Industry/Entity Type
Education
Requirements
Must have
- company logo and company name (see attached file)

```html
<!DOCTYPE html>
<html lang="en">
<head>
<meta charset="utf-8">
<title>Maple Crest Tutoring Flyers</title>
<link href="https://fonts.googleapis.com/css2?family=Cinzel:wght@400;600&family=Delius&family=Open+Sans:ital,wght@0,400;0,600;0,700;1,700&display=swap" rel="stylesheet">
<style>
:root{
  --red:#c21d33;
  --yellow:#fdca2c;
  --yellow-deep:#f2b613;
  --cream:#fde59a;
  --ink:#111;
  --night:#231f20;
  --olive:#a0801d;
  --dot:#a88a2a;
  --board:#5f6b66;
  --board-dark:#3c3f40;
  --white:#fff;
}
*{margin:0;padding:0;box-sizing:border-box}
html,body{width:1200px;height:900px;overflow:hidden;background:var(--white)}
body{position:relative;font-family:"Open Sans",Arial,sans-serif}
.flyer{position:absolute;top:144px;width:396px;height:612px;overflow:hidden;background:var(--yellow)}
.flyer--math{left:168px}
.flyer--exam{left:637px}
.abs{position:absolute}
.photo{position:absolute;left:0;width:396px}
.flyer--math .photo{top:46px;height:175px;background:linear-gradient(135deg,#7d8a84,var(--board) 55%,#4f5a55)}
.flyer--exam .photo{top:47px;height:193px;background:linear-gradient(90deg,#6a6d6c,var(--board-dark) 50%,#2f3131)}
.shape{position:absolute;left:0;top:0}
.headline-math{left:2px;top:68px;width:160px;height:50px;line-height:50px;text-align:center;color:var(--white);font-family:"Cinzel",serif;font-size:44px;transform:rotate(-45deg);transform-origin:center;letter-spacing:1px;white-space:nowrap}
.subhead{left:44px;top:183px;color:var(--red);font-family:"Cinzel",serif;font-size:27px;white-space:nowrap}
.tagline{left:197px;top:222px;width:199px;height:53px;background:var(--cream);padding:6px 0 0 20px;font-weight:700;font-style:italic;font-size:17.5px;line-height:20px;color:var(--ink)}
.courses{left:18px;top:286px;list-style:none;font-family:"Delius",cursive;font-size:15.5px;letter-spacing:-0.4px;line-height:25.5px;color:var(--ink);white-space:nowrap}
.courses li{position:relative;padding-left:17px}
.courses li::before{content:"";position:absolute;left:0;top:9px;width:9px;height:9px;background:var(--cream)}
.promo{position:absolute}
.promo-title{background:var(--cream);color:var(--red)}
.promo-line{color:var(--red);font-size:10px;font-weight:600;line-height:12px}
.promo-box{background:rgba(253,229,154,.85)}
.flyer--math .promo{left:0;top:410px}
.flyer--math .promo-title{width:236px;height:22px;font-size:16px;font-weight:600;padding:2px 0 0 17px}
.flyer--math .promo-box{width:236px;padding:2px 0 2px 17px}
.flyer--math .promo-box2{width:259px;padding:2px 0 2px 17px;background:rgba(253,229,154,.85)}
.brand{left:272px;top:420px;width:112px;display:flex;flex-direction:column;align-items:center;gap:6px;color:var(--red);font-weight:700;font-size:14px;text-align:center;line-height:16px}
.brand-mark{width:26px;height:26px;background:var(--red)}
.pin-art{left:102px;top:536px;width:80px;height:56px;background:linear-gradient(135deg,#f4e6a5,#7cc5c0 60%,#d44f8a);border-radius:4px}
.contact-math{left:192px;top:540px;color:var(--white);font-size:9px;font-weight:600;line-height:11.5px}
.contact-math td{vertical-align:top;padding:0}
.contact-math td:first-child{width:32px}
.band-exam{left:0;top:0;width:396px;height:47px;background:var(--red);color:var(--white);font-family:"Cinzel",serif;font-size:36px;text-align:center;line-height:48px}
.headline-exam{left:34px;top:182px;color:var(--red);font-family:"Cinzel",serif;font-size:48px;letter-spacing:-1px;white-space:nowrap;line-height:54px}
.pitch{left:21px;top:248px;font-weight:700;font-style:italic;font-size:23.5px;line-height:29px;color:var(--ink);white-space:nowrap}
.exams{left:118px;top:313px;display:grid;grid-template-columns:132px 120px;row-gap:8px;color:var(--red);font-weight:700;font-size:32px;line-height:38px}
.exams span{position:relative;padding-left:18px}
.exams span::before{content:"";position:absolute;left:0;top:16px;width:9px;height:9px;border-radius:50%;background:var(--dot)}
.flyer--exam .promo{left:0;top:434px}
.flyer--exam .promo-title{width:236px;height:24px;font-family:"Delius",cursive;font-size:16px;padding:3px 0 0 18px;color:var(--ink)}
.flyer--exam .promo-box{width:260px;padding:3px 0 3px 18px}
.contact-exam{left:18px;top:529px;list-style:none;font-size:9.5px;font-weight:600;line-height:14px;color:var(--ink)}
.contact-exam li{display:flex;align-items:center;gap:6px}
.contact-exam svg{width:8px;height:8px;fill:var(--red)}
.foot-exam{left:0;top:594px;width:396px;height:18px;background:var(--olive)}
</style>
</head>
<body>

<section class="flyer flyer--math" aria-label="Math tutoring flyer">
  <div class="photo" role="img" aria-label="Photo of a student scratching his head in front of a chalkboard covered in equations"></div>
  <svg class="shape" width="396" height="612" viewBox="0 0 396 612" aria-hidden="true">
    <polygon points="0,0 396,0 396,46 155,46 0,221" fill="var(--red)"/>
    <polygon points="0,221 396,221 396,612 0,612" fill="var(--yellow)"/>
    <polygon points="0,561 396,478 396,612 0,612" fill="var(--night)"/>
  </svg>
  <div class="abs headline-math">MATH</div>
  <div class="abs subhead">to Abstract Concrete</div>
  <div class="abs tagline">We can help make<br>the connection</div>
  <ul class="abs courses">
    <li>Ontario Math G.9 – 12</li>
    <li>IB Math High Level , Standard Level, Math Studies</li>
    <li>AP Calculus AB/BC</li>
    <li>University Year 1 Calculus</li>
  </ul>
  <div class="promo">
    <div class="promo-title">Promotional Offer:</div>
    <div class="promo-box promo-line">Free Trial Lesson<br>(Try us out before you enrol!</div>
    <div class="promo-box2 promo-line">Call or email us today for a Free Trial Lesson.)</div>
  </div>
  <div class="abs brand"><span class="brand-mark"></span>Maple Crest Tutoring</div>
  <div class="abs pin-art" role="img" aria-label="Illustration of a map with a location pin"></div>
  <table class="abs contact-math">
    <tr><td>Add</td><td>: 120 Birchwood Avenue, Unit 4<br>&nbsp;&nbsp;Lakeview, ON A1B 2C3</td></tr>
    <tr><td>Email</td><td>: Service@MapleCrestTutoring.com</td></tr>
    <tr><td>Tel</td><td>: 555-014-2260</td></tr>
    <tr><td>Web</td><td>: www.MapleCrestTutoring.com</td></tr>
  </table>
</section>

<section class="flyer flyer--exam" aria-label="Exam preparation flyer">
  <div class="abs band-exam">EXAM</div>
  <div class="photo" role="img" aria-label="Photo of a thoughtful student beside a chalkboard with algebra fractions"></div>
  <svg class="shape" width="396" height="612" viewBox="0 0 396 612" aria-hidden="true">
    <rect x="0" y="240" width="396" height="372" fill="var(--yellow)"/>
    <path d="M0,300 C60,380 160,420 260,420 C330,420 370,440 396,460 L396,612 L0,612 Z" fill="var(--yellow-deep)"/>
  </svg>
  <div class="abs headline-exam">PREPARATION</div>
  <div class="abs pitch">Come out on TOP. We can help.<br>SCORE! With our help.</div>
  <div class="abs exams"><span>SAT</span><span>PSAT</span><span>SSAT</span><span>OSSLT</span></div>
  <div class="promo">
    <div class="promo-title">Promotional Offer:</div>
    <div class="promo-box promo-line">Free Trial Lesson<br>(Try us out before you enrol!<br>Call or email us today for a Free Trial Lesson.)</div>
  </div>
  <ul class="abs contact-exam">
    <li><svg viewBox="0 0 10 10"><path d="M5 0a3.5 3.5 0 0 0-3.5 3.5C1.5 6 5 10 5 10s3.5-4 3.5-6.5A3.5 3.5 0 0 0 5 0zm0 5a1.5 1.5 0 1 1 0-3 1.5 1.5 0 0 1 0 3z"/></svg>120 Birchwood Avenue, Unit 4, Lakeview, ON A1B 2C3</li>
    <li><svg viewBox="0 0 10 10"><path d="M0 2h10v6H0z M0 2l5 3.5L10 2" /></svg>Service@MapleCrestTutoring.com</li>
    <li><svg viewBox="0 0 10 10"><path d="M2 0l2 2.5-1 1.2c.7 1.4 1.8 2.5 3.3 3.3l1.2-1L10 8l-1.5 2C4 9.5.5 6 0 1.5z"/></svg>555-014-2260</li>
    <li><svg viewBox="0 0 10 10"><circle cx="5" cy="5" r="5"/></svg>www.MapleCrestTutoring.com</li>
  </ul>
  <div class="abs foot-exam"></div>
</section>

</body>
</html>
```